Banners for slider on first page of the website

We need up to 3 different banners for our website: www.trelk.si
Current design is maybe a bit too playful, so do not mind on it. It can include some natural elements
1) Design needs to be modern type
2) Has to include products which are on our website
3) Has to be in two sizes: mobile and web - like we have now
4) Each slider CAN represent each category we have or CAN include multiple
5) Optional text holders

```html
<!DOCTYPE html>
<html lang="sl">
<head>
<meta charset="utf-8">
<title>Trelk kozmetika – Bubble Bath</title>
<link href="https://fonts.googleapis.com/css2?family=Josefin+Sans:wght@400;600;700&family=Poppins:wght@400;500;600&display=swap" rel="stylesheet">
<style>
  :root {
    --pink: #f266ad;
    --pink-soft: #f7a9cf;
    --pink-badge: #f59cc8;
    --pink-product: #e8338f;
    --ink: #2b2b2b;
    --white: #ffffff;
    --mist: #f5f4f4;
    --window: #eef0f0;
    --leaf: #8e9a6a;
    --tub: #c9a58a;
    --tub-light: #e6d3c4;
    --skin: #d9b49c;
    --foam: #f7f4f2;
  }
  * { box-sizing: border-box; margin: 0; padding: 0; }
  html, body { width: 1200px; height: 544px; overflow: hidden; background: var(--white); }
  body { font-family: "Poppins", sans-serif; color: var(--ink); position: relative; }

  .topbar {
    height: 28px; background: var(--pink-soft);
    display: flex; align-items: center; padding: 0 42px;
    font-size: 10px; color: var(--white);
  }
  .topbar .contact { display: flex; align-items: center; gap: 5px; }

  .mainnav {
    height: 52px; display: flex; align-items: center; justify-content: space-between;
    padding: 0 40px; position: relative; font-size: 11px; font-weight: 500;
  }
  .mainnav .links { display: flex; gap: 32px; }
  .mainnav .links span.dropdown::after { content: " ˅"; font-size: 8px; }
  .brand {
    position: absolute; left: 50%; top: 50%; transform: translate(-50%, -50%);
    display: flex; align-items: center; gap: 5px;
    font-family: "Josefin Sans", sans-serif; font-weight: 700; font-size: 14px;
    color: var(--pink); letter-spacing: 1px;
  }
  .brand .dot { width: 16px; height: 16px; border-radius: 50%; background: var(--pink); }
  .tools { display: flex; align-items: center; gap: 20px; font-weight: 600; }
  .tools .item { display: flex; align-items: center; gap: 4px; }
  .badge {
    width: 13px; height: 13px; border-radius: 50%; background: var(--pink-badge);
    color: var(--white); font-size: 8px; display: inline-flex; align-items: center; justify-content: center;
  }

  .hero { position: absolute; top: 80px; left: 0; width: 1200px; height: 458px; overflow: hidden; }
  .hero .bg-circle {
    position: absolute; left: -40px; top: 140px; width: 250px; height: 250px;
    border-radius: 50%; background: var(--mist);
  }
  .hero .photo {
    position: absolute; left: 486px; top: 0; width: 714px; height: 458px;
    background:
      linear-gradient(90deg, var(--white) 0%, rgba(255,255,255,0.85) 4%, rgba(255,255,255,0) 16%),
      linear-gradient(160deg, rgba(232,51,143,0) 78%, var(--pink-product) 79%, var(--pink-product) 100%),
      linear-gradient(180deg,
        var(--window) 0%,
        var(--leaf) 14%,
        var(--window) 28%,
        var(--skin) 40%,
        var(--tub) 54%,
        var(--tub-light) 68%,
        var(--foam) 80%,
        var(--white) 100%);
  }
  .hero .copy { position: absolute; left: 100px; top: 133px; font-family: "Josefin Sans", sans-serif; color: var(--pink); }
  .hero .eyebrow { font-size: 22px; font-weight: 600; letter-spacing: 1px; }
  .hero h1 { font-size: 45px; font-weight: 700; letter-spacing: 2px; margin-top: 14px; line-height: 1; }
  .hero .lead { font-size: 17px; font-weight: 700; letter-spacing: 1px; line-height: 1.3; margin-top: 22px; text-transform: uppercase; }

  .baseline { position: absolute; left: 0; top: 538px; width: 1200px; height: 6px; background: var(--pink-soft); }
</style>
</head>
<body>
  <header>
    <div class="topbar">
      <div class="contact">
        <svg width="10" height="8" viewBox="0 0 10 8" fill="none" stroke="currentColor" stroke-width="1"><rect x="0.5" y="0.5" width="9" height="7"/><path d="M0.5 0.5 5 4.5 9.5 0.5"/></svg>
        info@trelk.si
      </div>
    </div>
    <nav class="mainnav">
      <div class="links"><span>Domov</span><span class="dropdown">Trgovina</span></div>
      <div class="brand"><span class="dot"></span>TRELK</div>
      <div class="tools">
        <span class="item">
          <svg width="11" height="12" viewBox="0 0 11 12" fill="none" stroke="currentColor" stroke-width="1.2"><rect x="1" y="5" width="9" height="6" rx="1"/><path d="M3 5V3.5a2.5 2.5 0 0 1 5 0V5"/></svg>
          Vpiši se
        </span>
        <svg width="12" height="12" viewBox="0 0 12 12" fill="none" stroke="currentColor" stroke-width="1.3"><circle cx="5" cy="5" r="3.8"/><path d="M8 8l3 3"/></svg>
        <span class="item">
          <svg width="12" height="11" viewBox="0 0 12 11" fill="none" stroke="currentColor" stroke-width="1.2"><path d="M6 10 1.5 5.5a2.6 2.6 0 0 1 4.5-3 2.6 2.6 0 0 1 4.5 3z"/></svg>
          <span class="badge">0</span>
        </span>
        <span class="item">€0,00
          <svg width="12" height="12" viewBox="0 0 12 12" fill="none" stroke="currentColor" stroke-width="1.2"><rect x="1.5" y="4" width="9" height="7" rx="1"/><path d="M4 4V3a2 2 0 0 1 4 0v1"/></svg>
          <span class="badge">0</span>
        </span>
      </div>
    </nav>
  </header>

  <section class="hero">
    <div class="bg-circle"></div>
    <div class="photo" role="img" aria-label="Photo of a woman relaxing in a foamy bubble bath by a window with a plant, a pink Bubble Bath bottle in the lower right corner"></div>
    <div class="copy">
      <p class="eyebrow">PRODUCT SPOTLIGHT</p>
      <h1>BUBBLE BATH</h1>
      <p class="lead">Privoščite si dolgo vroče<br>namakanje z obilico mehurčkov,<br>eteričnih olj vrtnice in cedre.</p>
    </div>
  </section>
  <div class="baseline"></div>
</body>
</html>
```